Design a single page Shopify store web page

We are looking to have a page designed for a single page Shopify store with 2 products. We already have a basic structure that we like, though we are open to suggestions. We are looking for somebody to provide a design/color scheme that we can then implement using Shopify's templating system. We can handle the implementation(HTML / CSS / jS) as we already have 2 web developers on the team, but have not been able to find a design we liked.

The job would consist of providing a mockup (photoshop or otherwise) and any vector graphics you choose to create for the site (we can provide product photos and other images).

You can also look at http://brickwellgoods.com.au for some of our design direction we have used so far

Target Market(s)

Young Australian Males (18 - 49)

Industry/Entity Type

Store

Number of Pages Required

1 page

Font styles to use
Serif
Sans Serif

Requirements
Must have
• Single Page Design
• E-commerce Product Purchase
• Manly (whatever interpretation of that you have)

```html
<!DOCTYPE html>
<html lang="en">
<head>
<meta charset="utf-8">
<title>Brickwell Goods – Underwear and Socks Plans</title>
<link rel="stylesheet" href="https://fonts.googleapis.com/css2?family=PT+Sans+Narrow:wght@400;700&family=PT+Sans:wght@400;700&display=swap">
<style>
:root{
  --gold:#d9a300;
  --ink:#1f2230;
  --ink-soft:#2a2e3d;
  --card:#272a37;
  --mist:#e8ebf3;
  --tile:#c9ccd6;
  --white:#ffffff;
  --text:#333333;
}
*{box-sizing:border-box;margin:0;padding:0}
html,body{width:960px;height:1200px;overflow:hidden;background:var(--white)}
body{font-family:"PT Sans",Arial,sans-serif;color:var(--text)}
.page{position:absolute;left:240px;top:0;width:480px;height:1200px;overflow:hidden}
.heading{font-family:"PT Sans Narrow","Arial Narrow",sans-serif;font-weight:700}
.accent{color:var(--gold)}

/* Hero */
.hero{position:relative;height:257px;background:linear-gradient(180deg,#5d6474 0%,#3f4556 55%,#2b2f3c 100%)}
.hero-photo{position:absolute;inset:0;background:radial-gradient(ellipse at 40% 35%,#8a8f9b 0%,#5a6070 45%,#353a48 100%);opacity:.85}
.topbar{position:absolute;left:0;top:0;width:480px;height:26px;background:rgba(31,34,48,.75)}
.brand{position:absolute;left:60px;top:4px;font-family:"PT Sans Narrow",sans-serif;font-weight:700;font-size:17px;color:var(--gold)}
.nav{position:absolute;left:198px;top:6px;display:flex}
.nav a{font-family:"PT Sans Narrow",sans-serif;font-size:7px;color:var(--white);text-decoration:none;padding:4px 6px;text-transform:uppercase;line-height:7px}
.nav a.active{background:var(--gold)}
.signup{position:absolute;left:380px;top:6px;width:40px;height:15px;background:var(--gold);color:var(--white);font-family:"PT Sans Narrow",sans-serif;font-weight:700;font-size:7px;text-transform:uppercase;display:flex;align-items:center;justify-content:center}
.hero-title{position:absolute;left:0;top:137px;width:480px;text-align:center;color:var(--white);font-size:16px;line-height:19px}
.notify{position:absolute;left:60px;top:214px;width:360px;height:43px;background:rgba(31,34,48,.9)}
.notify-label{position:absolute;top:4px;font-size:5.5px;color:var(--gold);width:168px;text-align:center}
.notify-label.left{left:8px}.notify-label.right{left:186px}
.email-field{position:absolute;left:8px;top:19px;width:168px;height:15px;background:var(--white);font-size:7px;display:flex;align-items:center;justify-content:center;color:#222}
.notify-btn{position:absolute;left:186px;top:19px;width:167px;height:15px;background:var(--gold);font-size:7px;color:var(--white);display:flex;align-items:center;justify-content:center}

/* How it works */
.how{position:absolute;left:0;top:257px;width:480px;height:143px}
.section-title{text-align:center;font-size:11px;color:var(--ink);text-transform:uppercase}
.how .section-title{position:absolute;top:21px;width:480px}
.step{position:absolute;top:48px;width:118px;height:55px;background:var(--gold)}
.step svg{position:absolute;left:6px;top:10px}
.step h3{position:absolute;left:36px;top:9px;font-size:6px;color:var(--ink);text-transform:uppercase}
.step p{position:absolute;left:36px;top:17px;width:76px;font-size:5px;line-height:6px;color:var(--ink)}
.step-num{position:absolute;left:46px;top:46px;width:18px;height:18px;border-radius:50%;background:var(--white);border:1.5px solid var(--gold);font-size:7px;font-weight:700;display:flex;align-items:center;justify-content:center;color:var(--ink)}

/* Plans */
.plans{position:absolute;left:0;top:400px;width:480px;height:228px;background:var(--mist)}
.plans .section-title{position:absolute;top:12px;width:480px;font-size:13px}
.plan{position:absolute;top:37px;width:176px;height:123px;background:var(--tile);border-top:3px solid var(--ink)}
.plan-tag{position:absolute;top:-3px;height:14px;padding:0 10px;background:var(--ink);color:var(--white);font-size:6px;font-weight:700;display:flex;align-items:center}
.photo{position:absolute;border:2px solid #e6e7ec}
.price{position:absolute;top:100px;height:12px;width:29px;background:var(--ink);color:var(--white);font-size:6px;display:flex;align-items:center;justify-content:center}
.buy{position:absolute;top:100px;height:12px;width:30px;background:var(--gold);color:var(--white);font-size:6px;display:flex;align-items:center;justify-content:center}
.perks{position:absolute;left:60px;top:174px;width:360px;height:32px;background:var(--gold);display:flex;justify-content:space-between;align-items:center;padding:0 14px 0 6px}
.perk{position:relative;width:76px;height:17px;background:var(--ink);color:var(--white);font-size:4.4px;white-space:nowrap;display:flex;align-items:center;padding-left:22px}
.perk svg.icon{position:absolute;left:4px;top:3px}
.perk .tick{position:absolute;right:-7px;top:1.5px}

/* Photo feed */
.feed{position:absolute;left:0;top:628px;width:480px;height:152px}
.feed .section-title{position:absolute;top:23px;width:480px;font-size:13px;text-transform:none}
.thumb{position:absolute;top:56px;width:62px;height:61px;border:2px solid #d9dbe2}

/* FAQ */
.faq{position:absolute;left:0;top:780px;width:480px;height:256px;background:linear-gradient(135deg,#30343f 0%,#1f2230 60%,#262a36 100%)}
.faq .section-title{position:absolute;top:11px;width:480px;color:var(--gold);font-size:12px}
.faq-card{position:absolute;width:118px;height:88px;background:rgba(25,27,38,.92);padding:7px 6px;text-align:center}
.faq-card h3{font-size:8px;line-height:9.5px;color:var(--gold);margin-bottom:6px}
.faq-card p{font-size:5px;line-height:7px;color:#d5d7de}
.pager{position:absolute;top:236px;left:212px;display:flex;gap:6px;align-items:center}
.dot{width:7px;height:7px;border-radius:50%;background:#888}
.dot.on{background:var(--gold)}
.arrow{width:8px;height:8px;border-radius:50%;background:#111;display:flex;align-items:center;justify-content:center}

/* About */
.about{position:absolute;left:0;top:1036px;width:480px;height:128px;background:var(--gold);text-align:center}
.about .section-title{position:absolute;top:12px;width:480px;font-size:12px}
.about h3{position:absolute;top:36px;width:480px;font-size:10px;color:var(--ink)}
.about h3 .light{color:var(--white)}
.about .lead{position:absolute;top:49px;width:480px;font-size:7px;color:var(--ink)}
.about .body{position:absolute;left:60px;top:68px;width:360px;font-size:5px;line-height:7px;color:var(--ink)}

/* Footer */
.footer{position:absolute;left:0;top:1164px;width:480px;height:36px;background:var(--ink)}
.copyright{position:absolute;left:60px;top:16px;font-size:5px;color:var(--gold)}
.connect{position:absolute;left:364px;top:5px;font-size:5px;color:var(--gold)}
.socials{position:absolute;left:368px;top:14px;display:flex;gap:4px}
.socials span{width:12px;height:12px;background:var(--gold)}
</style>
</head>
<body>
<div class="page">

  <header class="hero">
    <div class="hero-photo" role="img" aria-label="Photo of two young men in open shirts and underwear leaning against a tiled wall"></div>
    <div class="topbar">
      <div class="brand">Brickwell Goods</div>
      <nav class="nav">
        <a class="active" href="#how">How it works</a>
        <a href="#plans">Plans</a>
        <a href="#faq">FAQ</a>
        <a href="#about">About us</a>
      </nav>
      <div class="signup">Sign up</div>
    </div>
    <h1 class="hero-title heading">New <span class="accent">Underwear</span> and <span class="accent">Socks</span> Delivered to<br>Your Door Every <span class="accent">3</span> or <span class="accent">6</span> Month</h1>
    <div class="notify">
      <div class="notify-label left">Let me know when you launch</div>
      <div class="notify-label right">Get a free gift with your first pack</div>
      <div class="email-field">Enter Your Email</div>
      <div class="notify-btn">Notify Me</div>
    </div>
  </header>

  <section class="how" id="how">
    <h2 class="section-title heading">How it works</h2>
    <div class="step" style="left:60px">
      <svg width="26" height="24" viewBox="0 0 26 24"><rect x="1" y="5" width="18" height="18" fill="none" stroke="#1f2230" stroke-width="2"/><path d="M5 13l5 6L24 1" fill="none" stroke="#1f2230" stroke-width="2.5"/></svg>
      <h3>Choose a plan</h3>
      <p>There will be plans for all budgets and styles.</p>
      <div class="step-num">1</div>
    </div>
    <div class="step" style="left:181px">
      <svg width="24" height="26" viewBox="0 0 24 26"><path d="M8 24V6a2 2 0 014 0v8l8 2v6l-3 2z" fill="none" stroke="#1f2230" stroke-width="1.8"/><circle cx="10" cy="6" r="5" fill="none" stroke="#1f2230" stroke-width="1"/></svg>
      <h3>Choose how often</h3>
      <p>Decide whether you would like to receive new packages every 3 or 6 months.</p>
      <div class="step-num">2</div>
    </div>
    <div class="step" style="left:302px">
      <svg width="26" height="22" viewBox="0 0 26 22"><rect x="9" y="2" width="15" height="11" fill="#1f2230"/><path d="M1 14h8l6 2h8v3H11l-10-2z" fill="#1f2230"/></svg>
      <h3>Get your pack</h3>
      <p>We'll send out your first pack right away and then again every 3 or 6 months.</p>
      <div class="step-num">3</div>
    </div>
  </section>

  <section class="plans" id="plans">
    <h2 class="section-title heading">Plan</h2>
    <article class="plan" style="left:60px">
      <div class="plan-tag" style="left:0">Comfort</div>
      <div class="photo" role="img" aria-label="Photo of blue trunks with a printed waistband" style="left:10px;top:23px;width:74px;height:57px;background:linear-gradient(135deg,#2aa6c8,#137a9c)"></div>
      <div class="photo" role="img" aria-label="Photo of white briefs" style="left:109px;top:20px;width:50px;height:30px;background:linear-gradient(135deg,#e9e9ea,#b9bbc0)"></div>
      <div class="photo" role="img" aria-label="Photo of grey striped socks" style="left:109px;top:53px;width:50px;height:33px;background:linear-gradient(135deg,#7b7f88,#3b3e45)"></div>
      <div class="price" style="left:90px">$ 40</div>
      <div class="buy" style="left:120px">Get it !</div>
    </article>
    <article class="plan" style="left:242px">
      <div class="plan-tag" style="right:0">Style</div>
      <div class="photo" role="img" aria-label="Photo of folded grey socks" style="left:16px;top:20px;width:50px;height:33px;background:linear-gradient(135deg,#9a9ca3,#55585f)"></div>
      <div class="photo" role="img" aria-label="Photo of purple trunks" style="left:16px;top:56px;width:50px;height:30px;background:linear-gradient(135deg,#4a3b66,#2b2340)"></div>
      <div class="photo" role="img" aria-label="Photo of legs wearing patterned socks on a red floor" style="left:72px;top:20px;width:93px;height:71px;background:linear-gradient(135deg,#b4654a,#6e3a2e)"></div>
      <div class="price" style="left:18px">$ 45</div>
      <div class="buy" style="left:48px">Get it !</div>
    </article>
    <div class="perks">
      <div class="perk"><svg class="icon" width="16" height="11" viewBox="0 0 16 11"><rect x="0" y="1" width="10" height="7" fill="#fff"/><path d="M10 3h3l3 3v2h-6z" fill="#fff"/><circle cx="3" cy="9" r="1.6" fill="#fff"/><circle cx="12" cy="9" r="1.6" fill="#fff"/></svg>Free Shipping<svg class="tick" width="14" height="14" viewBox="0 0 14 14"><circle cx="7" cy="7" r="6.5" fill="#d9a300" stroke="#1f2230"/><path d="M3.5 7l2.5 2.5 4.5-5" fill="none" stroke="#1f2230" stroke-width="1.6"/></svg></div>
      <div class="perk"><svg class="icon" width="16" height="11" viewBox="0 0 16 11"><rect x="3" y="2" width="10" height="8" fill="#fff"/><path d="M1 5l3-3v6z" fill="#fff"/></svg>Easy Returns<svg class="tick" width="14" height="14" viewBox="0 0 14 14"><circle cx="7" cy="7" r="6.5" fill="#d9a300" stroke="#1f2230"/><path d="M3.5 7l2.5 2.5 4.5-5" fill="none" stroke="#1f2230" stroke-width="1.6"/></svg></div>
      <div class="perk"><svg class="icon" width="16" height="11" viewBox="0 0 16 11"><circle cx="8" cy="5.5" r="5" fill="#fff"/><path d="M5.5 3l5 5M10.5 3l-5 5" stroke="#1f2230" stroke-width="1.4"/></svg>Cancel Whenever<svg class="tick" width="14" height="14" viewBox="0 0 14 14"><circle cx="7" cy="7" r="6.5" fill="#d9a300" stroke="#1f2230"/><path d="M3.5 7l2.5 2.5 4.5-5" fill="none" stroke="#1f2230" stroke-width="1.6"/></svg></div>
      <div class="perk"><svg class="icon" width="16" height="11" viewBox="0 0 16 11"><circle cx="8" cy="5.5" r="5" fill="#fff"/><circle cx="8" cy="5.5" r="2.5" fill="#1f2230"/></svg>Satisfaction Guaranteed<svg class="tick" width="14" height="14" viewBox="0 0 14 14"><circle cx="7" cy="7" r="6.5" fill="#d9a300" stroke="#1f2230"/><path d="M3.5 7l2.5 2.5 4.5-5" fill="none" stroke="#1f2230" stroke-width="1.6"/></svg></div>
    </div>
  </section>

  <section class="feed">
    <h2 class="section-title heading">What’s up on our photo feed?</h2>
    <div class="thumb" role="img" aria-label="Photo of leather shoes with red socks" style="left:60px;background:linear-gradient(135deg,#6b5038,#2c2420)"></div>
    <div class="thumb" role="img" aria-label="Photo of boots with patterned socks" style="left:134px;background:linear-gradient(135deg,#3e4b6a,#1d2232)"></div>
    <div class="thumb" role="img" aria-label="Photo of a rolled pair of navy socks" style="left:209px;background:linear-gradient(135deg,#2b3a66,#161c30)"></div>
    <div class="thumb" role="img" aria-label="Photo of striped socks laid in a row" style="left:283px;background:linear-gradient(135deg,#3c6a7a,#7a3c4a)"></div>
    <div class="thumb" role="img" aria-label="Photo of colourful socks laid out on a table" style="left:358px;background:linear-gradient(135deg,#2f5f6e,#5a3a2a)"></div>
  </section>

  <section class="faq" id="faq">
    <h2 class="section-title heading">FAQ</h2>
    <div class="faq-card" style="left:60px;top:40px"><h3 class="heading">What is Brickwell Goods?</h3><p>Brickwell Goods is an Australian subscription service for men's underwear and socks. We stock all your favourite brands and have a range of plans for all budgets and styles.</p></div>
    <div class="faq-card" style="left:181px;top:40px"><h3 class="heading">What is your<br>Satisfaction Guarantee</h3><p>We consider Brickwell Goods to be a premium service and customer service is key to that. If for any reason you aren't satisfied simply return your package for a full refund of the charge. In the case of a recurring package we'll refund the most recent charge.</p></div>
    <div class="faq-card" style="left:302px;top:40px"><h3 class="heading">What Is Brickwell Goods?</h3><p>Shipping is free Australia wide. We ship all of our packages within 48 hours of payment Monday–Friday. All our packs are shipped through Coastline Post with tracking.</p></div>
    <div class="faq-card" style="left:60px;top:138px"><h3 class="heading">What do I get with my<br>Brickwell Plan?</h3><p>You'll get 3 pairs of underwear and 3 pairs of socks. You select the frequency of deliveries when you sign up.</p></div>
    <div class="faq-card" style="left:181px;top:138px"><h3 class="heading">Return Policy</h3><p>We have a 30 day return policy. To be eligible for a return, your item must be unused and in the same condition that you received it. If you need to make a return simply email hello@brickwellgoods.com.au</p></div>
    <div class="faq-card" style="left:302px;top:138px"><h3 class="heading">What Brands do you<br>Stock?</h3><p>Brickwell Goods currently stocks Harbourline, Kestrel, Marlowe Grey, Fenwick &amp; Co and Tall Timber. Is your favourite brand missing? Let us know hello@brickwellgoods.com.au</p></div>
    <div class="pager">
      <div class="arrow"><svg width="4" height="5" viewBox="0 0 4 5"><path d="M3 0L0 2.5 3 5" fill="none" stroke="#fff"/></svg></div>
      <div class="dot on"></div><div class="dot"></div>
      <div class="arrow"><svg width="4" height="5" viewBox="0 0 4 5"><path d="M1 0l3 2.5L1 5" fill="none" stroke="#fff"/></svg></div>
    </div>
  </section>

  <section class="about" id="about">
    <h2 class="section-title heading" style="color:var(--ink)">About us</h2>
    <h3 class="heading">We've Got <span class="light">Plans</span> for Every <span class="light">Man</span></h3>
    <p class="lead">We'll be customising plans for every budget and style. Sign up we'll make it easy to keep your bare essentials fresh.</p>
    <p class="body">Every pack is picked by our team and sent in plain, sturdy packaging. Pause, swap or cancel your plan at any time from your account. We only stock labels we wear ourselves, so you can count on comfort, fit and fabric that lasts from one delivery to the next.</p>
  </section>

  <footer class="footer">
    <div class="copyright">© Brickwell Goods 2014</div>
    <div class="connect">Connect with us</div>
    <div class="socials"><span></span><span></span><span></span></div>
  </footer>

</div>
</body>
</html>
```